Young Accounting firm needing a captivating business card

We need a business card design that forces the person to look at the card because its either gold foil, plastic, or lettering pop up etc. We already have a logo with a specific gold color and we need to make it pop. We are an accounting firm. I need the words" accounting, payroll, licenses, audits, taxes" somewhere on the business card so as to describe what we do- preferably on the side where the logo is at.

Industry/Entity Type

Accounting

Contact Information for Business Card

Address 48276 9th Ave S Ste 305, Federal Way, WA 98117
Business Phone (360)418-2096
Fax (360)418-2157
Office Cell Phone (360)586-7319

Font styles to use
Serif

Colors
85abd2

Requirements
Must have
• It should state
• "Accounting" "Taxes" "Audits" "Licenses" "Payroll"
Nice to have
• Matte with gold foil, different textures, With Either a textured ivory background or gray blue slate background
Should not have
• colorful colors

```html
<!DOCTYPE html>
<html lang="en">
<head>
<meta charset="utf-8">
<title>Harbor Ledger — Business Card</title>
<link href="https://fonts.googleapis.com/css2?family=Quicksand:wght@500;600;700&display=swap" rel="stylesheet">
<style>
  :root {
    --backdrop: #0e0f11;
    --gold: #a88a2c;
    --gold-foil: #b8952e;
    --paper-top: #e6e6e6;
    --paper-bottom: #d3d2d3;
    --ink-grey: #6b6b6b;
    --slate: #1c1c1d;
    --band-text: #f4efe0;
  }
  * { margin: 0; padding: 0; box-sizing: border-box; }
  html, body {
    width: 1200px; height: 1051px; overflow: hidden;
    background: var(--backdrop);
    font-family: "Quicksand", sans-serif;
  }
  .canvas { position: relative; width: 1200px; height: 1051px; }

  /* Front: contact side */
  .card-front {
    position: absolute; left: 156px; top: 256px;
    width: 308px; height: 539px;
    background: linear-gradient(180deg, var(--paper-top), var(--paper-bottom));
  }
  .brand {
    position: absolute; left: 0; right: 0; top: 33px;
    display: flex; flex-direction: column; align-items: center;
  }
  .brand-square { width: 56px; height: 56px; background: var(--gold); }
  .brand-name {
    margin-top: 18px; font-size: 30px; font-weight: 700;
    color: var(--gold); letter-spacing: -0.5px; line-height: 1;
  }
  .person { position: absolute; left: 24px; top: 237px; }
  .person-name { font-size: 16.5px; font-weight: 700; color: var(--gold); line-height: 1.1; }
  .person-role { font-size: 13px; font-weight: 500; color: var(--ink-grey); margin-top: 3px; }
  .phones { position: absolute; left: 24px; top: 309px; font-size: 13px; line-height: 17px; color: var(--ink-grey); font-weight: 500; }
  .phones .label { color: var(--gold); font-weight: 700; }
  .address { position: absolute; left: 24px; top: 387px; font-size: 13px; line-height: 17px; color: var(--ink-grey); font-weight: 500; }
  .email { position: absolute; left: 24px; top: 451px; font-size: 13px; color: var(--ink-grey); font-weight: 500; }
  .email strong { color: var(--gold); font-weight: 700; }
  .services-band {
    position: absolute; left: 0; bottom: 0; width: 100%; height: 42px;
    background: var(--gold); color: var(--band-text);
    display: flex; align-items: center; justify-content: center;
    font-size: 11.6px; font-weight: 500; white-space: nowrap;
  }

  /* Back: foil logo side */
  .card-back {
    position: absolute; left: 504px; top: 486px;
    width: 539px; height: 307px;
    background: var(--slate);
    display: flex; flex-direction: column; align-items: center;
  }
  .card-back .brand-square { margin-top: 85px; width: 70px; height: 70px; background: var(--gold-foil); }
  .card-back .brand-name { margin-top: 22px; font-size: 40px; color: var(--gold-foil); }
</style>
</head>
<body>
<main class="canvas">
  <section class="card-front">
    <div class="brand">
      <div class="brand-square"></div>
      <div class="brand-name">Harbor Ledger</div>
    </div>
    <div class="person">
      <div class="person-name">Marisol Vega</div>
      <div class="person-role">Account Manager</div>
    </div>
    <div class="phones">
      <div><span class="label">Office :</span> (360)586-7319</div>
      <div><span class="label">Business :</span> (360)418-2096</div>
      <div><span class="label">Fax :</span> (360)418-2157</div>
    </div>
    <div class="address">
      <div>48276 9th Ave S Ste 305,</div>
      <div>Federal Way, WA 98117</div>
    </div>
    <div class="email">info@<strong>harborledger</strong>.com</div>
    <div class="services-band">"Accounting" "Taxes" "Audits" "Licenses" "Payroll"</div>
  </section>

  <section class="card-back">
    <div class="brand-square"></div>
    <div class="brand-name">Harbor Ledger</div>
  </section>
</main>
</body>
</html>
```